New Air Taxi service needs an app design

We are in need of an app for a startup company called "Brisket Aviation". Think of Brisket Aviation as Zoomcar in the sky. (Please refer to the app Zoomcar for reference.)

For a low hourly rate, anyone can use our iphone app and schedule an impromptu regional flight from and to any airport. Even county and regional airports.

You can pay through the app, pick the departure and destination and see it the on a map where and when your plane (and pilot will arrive) Brisket Aviation uses Halvorn KT40's, the worlds most sophisticated and safest single engine airplane ever manufactured.

The Halvorn is a fast, comfortable, all composite 4 seat airplane that features an airframe parachute rescue systems on board. Quorbit "Halvorn KT40" for photos, info and creative inspiration. In the app, users must enter their passenger info, their weight 'naked', number of bags and the weight of their bags. Total weight cannot exceed 348 pounds and the app must check this.

They must pick their pickup location which for now will be either Westbrook Fenwick Airport, Elm Hollow SC Airport, Tavish NC Airport or Bexley NC Airport. Destination choices can be, Atlanta Gladewood Airport, Marlow Ashby Airport NC, Pendleford NC Airport, Corwin NC Airport.

For starters, we need to see screen shots of the app on paper to show investors. Logo is being created by others and winning design will be sent the new logo.

Target Market(s)

Business owners and professionals

Industry/Entity Type

It Company

Requirements
Must have
• See description
Nice to have
• See description
Should not have
• See description

```html
<!DOCTYPE html>
<html lang="en">
<head>
<meta charset="utf-8">
<title>Brisket Aviation – App Screens</title>
<link rel="stylesheet" href="https://fonts.googleapis.com/css2?family=Open+Sans:wght@300;400;600&display=swap">
<style>
:root{
  --page:#2c4552;
  --brand-blue:#0fa9f2;
  --sky-top:#163a72;
  --sky-mid:#2f63a3;
  --cloud:#b9d0e4;
  --sky-low:#6f9fc8;
  --ground:#3f6e8c;
  --white:#ffffff;
  --field:#eef0f3;
  --field-text:#6d7480;
  --panel:#f1f1f1;
  --text-dark:#2b2b2b;
  --map-a:#ede8db;
  --map-b:#e4e1cf;
  --map-c:#dfe6cf;
  --green:#2dbb4f;
  --red:#d9362c;
}
*{box-sizing:border-box;margin:0;padding:0}
html,body{width:1200px;height:882px;overflow:hidden}
body{background:var(--page);font-family:"Open Sans",Arial,sans-serif;position:relative}
.screen{position:absolute;top:208px;width:237px;height:423px;overflow:hidden;background:var(--sky-top)}
.screen--splash{left:96px}
.screen--login{left:480px}
.screen--map{left:864px;background:var(--white)}
.photo{position:absolute;inset:0;background:
  radial-gradient(ellipse 90px 60px at 40px 250px,rgba(215,230,242,.75),rgba(215,230,242,0)),
  radial-gradient(ellipse 120px 50px at 200px 390px,rgba(225,236,245,.7),rgba(225,236,245,0)),
  radial-gradient(ellipse 110px 80px at 70px 360px,rgba(200,205,210,.55),rgba(200,205,210,0)),
  linear-gradient(180deg,var(--sky-top) 0%,var(--sky-mid) 40%,var(--sky-low) 65%,var(--cloud) 82%,var(--ground) 100%)}
.status-bar{position:absolute;top:0;left:0;right:0;height:13px;display:flex;justify-content:space-between;align-items:center;padding:0 4px;font-size:8.5px;color:var(--white);z-index:2}
.status-bar .time{position:absolute;left:0;right:0;text-align:center}
.brand{position:absolute;left:0;right:0;display:flex;justify-content:center;align-items:center;gap:8px;color:var(--white);font-weight:300}
.brand-mark{width:16px;height:16px;border-radius:50%;background:var(--white)}
.screen--splash .brand{top:225px;font-size:24px}
.screen--login .brand{top:121px;font-size:22px}
.field{position:absolute;left:17px;width:204px;height:26px;border-radius:3px;background:var(--field);color:var(--field-text);font-size:10px;padding:6px 10px}
.field--email{top:225px}
.field--password{top:256px}
.btn-login{position:absolute;left:17px;top:302px;width:204px;height:29px;border-radius:3px;background:var(--brand-blue);color:var(--white);font-size:11px;font-weight:600;text-align:center;line-height:29px}
.link-forgot{position:absolute;top:335px;left:0;right:0;text-align:center;font-size:9px;color:var(--white)}
.signup-line{position:absolute;top:399px;left:0;right:0;text-align:center;font-size:10.5px;color:var(--white)}
.signup-line strong{font-weight:600}
.app-header{position:absolute;top:0;left:0;right:0;height:41px;background:var(--brand-blue)}
.app-header .title{position:absolute;top:17px;left:0;right:0;text-align:center;color:var(--white);font-size:14px}
.menu-dots{position:absolute;right:10px;top:19px}
.map{position:absolute;top:41px;left:0;right:0;height:327px;background:
  radial-gradient(ellipse 60px 45px at 120px 150px,var(--map-c),rgba(223,230,207,0)),
  linear-gradient(160deg,var(--map-a) 0%,var(--map-b) 50%,var(--map-a) 100%)}
.route{position:absolute;top:47px;left:6px;right:6px;height:42px;background:var(--panel);font-size:9px;color:var(--text-dark)}
.route .stop{position:absolute;left:18px;height:20px;line-height:20px;white-space:nowrap}
.route .stop--from{top:1px}
.route .stop--to{top:21px;background:var(--white);left:10px;right:0;padding-left:8px;box-shadow:0 1px 2px rgba(0,0,0,.15)}
.route .dot{position:absolute;left:8px;width:4px;height:4px;border-radius:50%}
.route .dot--from{top:9px;background:var(--green)}
.route .dot--to{top:29px;background:var(--red)}
.route .line{position:absolute;left:9.5px;top:13px;width:1px;height:16px;background:#999}
.eta-pin{position:absolute;left:143px;top:162px}
.plane-card{position:absolute;top:368px;left:0;right:0;height:55px;background:var(--white);border-top:1px solid #ddd}
.plane-thumb{position:absolute;left:8px;top:6px;width:44px;height:44px;background:linear-gradient(180deg,#a9c6e2,#d9dfe4)}
.plane-name{position:absolute;left:69px;top:14px;font-size:11.5px;line-height:13px;color:var(--text-dark)}
.plane-more{position:absolute;right:0;top:0;width:55px;height:55px;background:var(--panel);display:flex;align-items:center;justify-content:center}
</style>
</head>
<body>

<section class="screen screen--splash">
  <div class="photo" role="img" aria-label="Photo of a small propeller aircraft nose against a blue cloudy sky"></div>
  <div class="status-bar"><span>●●●○○ TELCO</span><span class="time">4:21 PM</span><span>100%</span></div>
  <div class="brand"><span class="brand-mark"></span><span>Brisket Aviation</span></div>
</section>

<section class="screen screen--login">
  <div class="photo" role="img" aria-label="Photo of a small propeller aircraft nose against a blue cloudy sky"></div>
  <div class="status-bar"><span>●●●○○ TELCO</span><span class="time">4:21 PM</span><span>100%</span></div>
  <div class="brand"><span class="brand-mark"></span><span>Brisket Aviation</span></div>
  <div class="field field--email">Email</div>
  <div class="field field--password">Password</div>
  <div class="btn-login">LOGIN</div>
  <div class="link-forgot">Forget Password?</div>
  <div class="signup-line">Don't have Account? <strong>Sign Up</strong></div>
</section>

<section class="screen screen--map">
  <div class="map" role="img" aria-label="Street map of the pickup area"></div>
  <div class="app-header">
    <div class="status-bar"><span>●●●○○ TELCO</span><span class="time">4:21 PM</span><span>100%</span></div>
    <div class="title">Brisket Aviation</div>
    <svg class="menu-dots" width="4" height="14" viewBox="0 0 4 14"><g fill="none" stroke="#fff" stroke-width="1"><circle cx="2" cy="2" r="1.3"/><circle cx="2" cy="7" r="1.3"/><circle cx="2" cy="12" r="1.3"/></g></svg>
  </div>
  <div class="route">
    <span class="dot dot--from"></span><span class="line"></span><span class="dot dot--to"></span>
    <div class="stop stop--from">BRV, 14 Larkfield Rd #1, Dunmore, NY</div>
    <div class="stop stop--to">OKL, 52 Fernway Rd, Oakridge Lake, NY</div>
  </div>
  <svg class="eta-pin" width="30" height="44" viewBox="0 0 30 44">
    <path d="M15 43 C11 34 1 27 1 15 A14 14 0 0 1 29 15 C29 27 19 34 15 43Z" fill="#0fa9f2"/>
    <circle cx="15" cy="15" r="10.5" fill="none" stroke="#fff" stroke-width="1"/>
    <text x="15" y="15" text-anchor="middle" font-family="Open Sans, sans-serif" font-size="9" fill="#fff">8</text>
    <text x="15" y="22" text-anchor="middle" font-family="Open Sans, sans-serif" font-size="5" fill="#fff">Min</text>
  </svg>
  <div class="plane-card">
    <div class="plane-thumb" role="img" aria-label="Photo of a parked single-engine aircraft"></div>
    <div class="plane-name">Halvorn KT40<br>G2 N417BK</div>
    <div class="plane-more">
      <svg width="18" height="18" viewBox="0 0 18 18"><circle cx="9" cy="9" r="8" fill="none" stroke="#222" stroke-width="1.2"/><path d="M7.5 5.5 L11 9 L7.5 12.5" fill="none" stroke="#222" stroke-width="1.3"/></svg>
    </div>
  </div>
</section>

</body>
</html>
```